FB and Youtube banner design for HVAC company

I would like an appealing site page banner for business page on Facebook (851w x 315h pixels) and one for youtube (2560w x 1440h pixels) for hvac company. Business card design and logo are attached. Company name is Silver Birch Air Conditioning, Refrigeration, and Heating.

NOTE: I put the business cards and log up to see some of the artwork the company is using. It's not to replicate that in the banner images.

Target Market(s)

Interested business and homeowner visitors to Facebook business page and youtube channel page.

Industry/Entity Type

Hvac

Font styles to use
Sans Serif

Requirements
Must have
• See logo for color scheme.
Should not have
• This should not look like a business card. Think of what is typically the banner on a facebook business page and youtube channel.

```html
<!DOCTYPE html>
<html lang="en">
<head>
<meta charset="utf-8">
<title>Silver Birch – Air Conditioning, Refrigeration, Heating</title>
<link rel="stylesheet" href="https://fonts.googleapis.com/css2?family=Roboto+Condensed:wght@700&display=swap">
<style>
  :root {
    --brand-blue: #2352b5;
    --brand-orange: #f26a21;
    --photo-light: #8e97c8;
    --photo-mid: #4f5c9c;
    --photo-dark: #252f63;
    --white: #ffffff;
    --ink: #1d2340;
  }
  * { margin: 0; padding: 0; box-sizing: border-box; }
  html, body { width: 1200px; height: 457px; overflow: hidden; background: var(--white); }
  .banner {
    position: relative;
    width: 1200px;
    height: 457px;
    overflow: hidden;
    font-family: "Roboto Condensed", "Arial Narrow", sans-serif;
    font-weight: 700;
  }
  .hero-photo {
    position: absolute;
    inset: 0;
    background:
      radial-gradient(ellipse 190px 150px at 190px 270px, rgba(180,188,228,0.55), transparent 75%),
      radial-gradient(ellipse 170px 120px at 440px 190px, rgba(180,188,228,0.5), transparent 75%),
      radial-gradient(ellipse 180px 110px at 800px 130px, rgba(180,188,228,0.5), transparent 75%),
      radial-gradient(ellipse 160px 120px at 1080px 60px, rgba(150,160,210,0.4), transparent 75%),
      linear-gradient(160deg, var(--photo-dark) 0%, var(--photo-mid) 45%, #3c4884 75%, var(--photo-dark) 100%);
  }
  .banner__art { position: absolute; inset: 0; display: block; }
  .services {
    position: absolute;
    top: 48px;
    left: 174px;
    display: flex;
    align-items: center;
    gap: 20px;
    color: var(--white);
    font-size: 30px;
    letter-spacing: 0.5px;
    text-transform: uppercase;
    font-weight: 700;
  }
  .services__dot {
    width: 15px; height: 15px;
    border-radius: 50%;
    background: var(--brand-orange);
  }
  .brand {
    position: absolute;
    left: 880px;
    top: 326px;
    width: 262px;
  }
  .brand__row { display: flex; align-items: center; gap: 14px; }
  .brand__mark {
    flex: none;
    width: 70px; height: 70px;
    border-radius: 50%;
    background: var(--brand-orange);
  }
  .brand__name {
    color: var(--brand-blue);
    font-size: 38px;
    line-height: 0.95;
    text-transform: uppercase;
    letter-spacing: 0.5px;
  }
  .brand__tagline {
    margin-top: 8px;
    color: var(--ink);
    font-size: 10.5px;
    letter-spacing: 0.9px;
    white-space: nowrap;
    text-transform: uppercase;
  }
</style>
</head>
<body>
<div class="banner">
  <div class="hero-photo" role="img" aria-label="Blue-tinted photo of outdoor air conditioning units on concrete pads beside a brick building"></div>

  <svg class="banner__art" viewBox="0 0 1200 457" width="1200" height="457" aria-hidden="true">
    <path class="swoosh swoosh--orange" fill="#f26a21"
          d="M0 457 L0 420 C 400 420, 700 360, 900 300 C 1000 270, 1100 238, 1200 224 L1200 457 Z"/>
    <path class="swoosh swoosh--blue" fill="#2352b5"
          d="M0 271 C 240 330, 460 385, 640 385 C 700 385, 760 375, 820 360 L820 457 L0 457 Z"/>
    <path class="swoosh swoosh--white" fill="#ffffff"
          d="M0 318 C 250 390, 480 405, 700 365 C 900 325, 1060 262, 1200 250 L1200 457 L0 457 Z"/>
  </svg>

  <h1 class="services">
    <span>Air Conditioning</span>
    <span class="services__dot"></span>
    <span>Refrigeration</span>
    <span class="services__dot"></span>
    <span>Heating</span>
  </h1>

  <div class="brand">
    <div class="brand__row">
      <span class="brand__mark"></span>
      <span class="brand__name">Silver<br>Birch</span>
    </div>
    <p class="brand__tagline">Air Conditioning • Refrigeration • Heating</p>
  </div>
</div>
</body>
</html>
```